7s Apex Harbour Rugby Squad

I need a website for a 7s Rugby team. 7s is a form of rugby union and one of the fastest rising sports in the world. Its recent addition to the Olympic games 2016 means that it's meteoric rise will only continue as more countries invest more money in their current programs as they compete for a chance at a medal.

See video for more insight: http://clipvault.example/watch/k9TqLm2RwZa

I've started and Elite, Invitation 7s team for U16 boys, U18 boys, and eventually, senior men and junior women's programs to compliment what we already have in place.

We are hoping to attract the top players in across our region of southern Ontario with the goal of created the top 7s rugby program in Canada and providing and ideal pathway for those that want to one day play for Canada.

I want a design that is bright, sharp, professional, flashy and has visual appeal.
Updates

Please see most recent uploaded photos and include these in your designs.  

Additionally, please have a look at the updated colour-scheme.

Thanks

Project Deadline Extended
Reason: Holidays and life have had consumed my energy and time. Would like to take the next week to complete this project with an appropriate amount of time and dedication. Thank you.

Please change images in all designs to include those I have uploaded.

Final decision made by the end of the weekend.

Prize will be increased and split.

Thank you for your patience and continued efforts.

Greatly appreciated.

Target Market(s)

Active people between the ages of 14 and 30.

Industry/Entity Type

Union

Font styles to use
Sans Serif

Colors
3176b5
cedeec
f04a50
cee9f6
ceddec
0255a3
5c5c5c
474747

Requirements
Must have
• Highly effective use of visuals; responsive theme or something similar.

Something to encourage players or those interested to want to learn more and potentially register for our affiliated rugby Academy, "Foremark Rugby Canada".

Nice to have
• Connection to YouTube Channel

```html
<!DOCTYPE html>
<html lang="en">
<head>
<meta charset="utf-8">
<title>Apex Harbour Sevens</title>
<link href="https://fonts.googleapis.com/css2?family=Source+Sans+3:wght@400;600;700&display=swap" rel="stylesheet">
<style>
:root{
  --blue:#3176b5;
  --blue-deep:#0255a3;
  --red:#f04a50;
  --red-hot:#f0304a;
  --ladder-bg:#dde6ec;
  --ink:#222;
  --grey:#5c5c5c;
  --grey-dark:#474747;
  --panel:#fff;
  --dark-panel:#1f1f1f;
}
*{box-sizing:border-box;margin:0;padding:0}
html,body{width:1200px;height:1077px;overflow:hidden}
body{font-family:"Source Sans 3",sans-serif;position:relative;background:#111}
.abs{position:absolute}
.stadium-bg{left:0;top:0;width:1200px;height:903px;
  background:radial-gradient(ellipse at 50% 95%,#3f7a2c 0%,#2c5a22 35%,#1b2a17 70%),#1b1b1b;}
.stadium-bg::before{content:"";position:absolute;left:0;top:0;right:0;height:260px;
  background:linear-gradient(180deg,#2a1d1d 0%,#5a2228 50%,rgba(60,40,35,0) 100%);}
.footer-bg{left:0;top:903px;width:1200px;height:174px;
  background:repeating-linear-gradient(180deg,#1a1a1a 0 2px,#222 2px 4px);}
.pole{width:5px;background:linear-gradient(90deg,#777,#ddd,#777)}
.flag{left:236px;top:24px;width:250px;height:134px;border-radius:6px 18px 10px 24px;
  background:linear-gradient(160deg,#fff 0%,#e9e9e9 60%,#cfcfcf 100%)}
.brand{left:236px;top:24px;width:250px;height:134px;display:flex;align-items:center;justify-content:center;
  color:var(--blue-deep);font-weight:700;font-size:30px;line-height:1;text-align:center}
.search{left:697px;top:22px;width:247px;height:31px;display:flex}
.search-field{flex:1;background:#fff;font-size:12px;color:#222;padding:9px 0 0 17px}
.search-go{width:45px;background:var(--blue);color:#fff;font-weight:700;font-size:13px;text-align:center;padding-top:7px}
.panel{left:204px;top:179px;width:792px;height:724px;background:var(--panel)}
.nav{left:204px;top:179px;width:792px;height:37px;background:linear-gradient(180deg,#3b82c4,#2a6aa6)}
.nav a{position:absolute;top:12px;color:#fff;font-weight:700;font-size:12px;text-decoration:none}
.nav .home{left:14px;top:3px;width:59px;height:30px;background:#1f3a55;border-radius:5px;text-align:center;padding-top:9px}
.nav .util{font-weight:600}
.nav .sep{position:absolute;left:723px;top:10px;width:2px;height:16px;background:#fff}
.hero-photo{left:214px;top:225px;width:532px;height:265px;
  background:linear-gradient(180deg,#5c9ad8 0%,#8fb7d0 25%,#d8b62c 45%,#c9a030 60%,#3a3a3a 70%,#444 100%)}
.hero-cta{left:746px;top:225px;width:239px;height:265px;background:var(--dark-panel);padding:26px 0 0 10px}
.hero-cta h1{color:var(--red-hot);font-weight:700;font-size:34px;line-height:42px}
.hero-cta p{color:#fff;font-weight:700;font-size:16px;line-height:20px;margin-top:14px;width:220px}
.ladder-head{left:218px;top:508px;width:215px;height:34px;background:#222}
.ladder-head span{position:absolute;left:0;top:0;width:154px;height:34px;background:var(--red-hot);
  clip-path:polygon(0 0,88% 0,100% 50%,88% 100%,0 100%);color:#fff;font-weight:700;font-size:12px;padding:9px 0 0 14px}
.ladder{left:218px;top:542px;width:215px;height:271px;background:var(--ladder-bg);padding:7px 0 0 13px;list-style:none}
.ladder li{display:flex;justify-content:space-between;width:187px;height:20px;font-weight:700;font-size:11.5px;color:#2a2a2a}
.section-title{color:#8a8a8a;font-weight:700;font-size:11px;letter-spacing:.1px}
.rule{height:1px;background:#aaa}
.date{left:461px;top:530px;width:40px;height:46px;border:1px solid #ddd;font-size:10.5px;color:#222;padding:7px 0 0 7px;line-height:20px}
.news-text{left:529px;top:540px;width:450px;font-size:10.5px;color:#333}
.thumb{width:192px;height:127px;border:2px solid #eee}
.thumb .img{width:100%;height:97px}
.thumb .cap{height:26px;background:#222;color:#eee;font-size:9.5px;padding:7px 0 0 10px;letter-spacing:.3px}
.sponsors{left:204px;top:836px;width:792px;height:67px;background:#e6e6e6;border-top:3px solid #d0d0d0}
.badge{background:#4a4a4a}
.footer-col h3{color:var(--blue);font-weight:700;font-size:11.5px;margin-bottom:5px}
.footer-col a{display:block;color:#fff;font-size:10.5px;line-height:20px;text-decoration:none}
.divider{width:0;border-left:1px dotted #888;top:925px;height:87px}
.legal{right:213px;top:919px;text-align:right;color:#ccc;font-size:10.5px;line-height:15px}
.legal a{color:#fff;text-decoration:none}
.footer-brand{left:796px;top:978px;width:175px;color:#9a9a9a;font-weight:700;font-size:24px;line-height:1;text-align:center}
</style>
</head>
<body>
<div class="abs stadium-bg" role="img" aria-label="Stadium crowd behind a green pitch, with sevens players in red running with the ball on both sides"></div>
<div class="abs footer-bg"></div>

<div class="abs pole" style="left:226px;top:8px;height:171px"></div>
<div class="abs pole" style="left:961px;top:8px;height:171px"></div>
<div class="abs flag" role="img" aria-label="White flag waving from the pole"></div>
<div class="abs brand">Apex Harbour<br>Sevens</div>

<div class="abs search"><div class="search-field">Search</div><div class="search-go">GO</div></div>

<div class="abs panel"></div>
<nav class="abs nav">
  <a class="home" href="#">HOME</a>
  <a href="#" style="left:93px">SCHEDULE</a>
  <a href="#" style="left:178px">TEAM</a>
  <a href="#" style="left:239px">GAME DAY</a>
  <a href="#" style="left:321px">FANS</a>
  <a class="util" href="#" style="left:683px">Login</a>
  <span class="sep"></span>
  <a class="util" href="#" style="left:738px">Photos</a>
</nav>

<div class="abs hero-photo" role="img" aria-label="Team in yellow jerseys posing behind a championship banner"></div>
<div class="abs hero-cta">
  <h1>JOIN RUGBY<br>SEVENS<br>TODAY</h1>
  <p>Season Memberships now available</p>
</div>

<div class="abs ladder-head"><span>LADDER</span></div>
<ul class="abs ladder">
  <li><span>Summits</span><span>0</span></li>
  <li><span>Rams</span><span>0</span></li>
  <li><span>Bluffs</span><span>0</span></li>
  <li><span>Voyagers</span><span>0</span></li>
  <li><span>Embers</span><span>0</span></li>
  <li><span>Lynxes</span><span>0</span></li>
  <li><span>Gales</span><span>0</span></li>
  <li><span>Marlins</span><span>0</span></li>
  <li><span>Wildflowers</span><span>0</span></li>
  <li><span>Tides</span><span>0</span></li>
  <li><span>Cyclones</span><span>0</span></li>
  <li><span>Rangers</span><span>0</span></li>
  <li><span>Western Surge</span><span>0</span></li>
</ul>

<div class="abs section-title" style="left:459px;top:505px">NEWS &amp; ACTIVITIES</div>
<div class="abs rule" style="left:572px;top:512px;width:413px"></div>
<div class="abs date">19<br>NOV</div>
<p class="abs news-text">Lorem ipsum dolor sit amet, consectetur adipiscing elit. Nullam sit amet quam metus, id iaculis mi.</p>

<div class="abs section-title" style="left:459px;top:613px">PHOTO STREAM</div>
<div class="abs rule" style="left:574px;top:621px;width:411px"></div>
<div class="abs thumb" style="left:461px;top:648px">
  <div class="img" role="img" aria-label="Team photo in yellow jerseys in a stadium" style="background:linear-gradient(180deg,#555 0%,#b03030 20%,#c8a43a 45%,#3b3b2a 75%,#4f8a3a 100%)"></div>
  <div class="cap">2013 Cyclones Team Photo,</div>
</div>
<div class="abs thumb" style="left:661px;top:648px">
  <div class="img" role="img" aria-label="Player diving to score a try on the grass" style="background:linear-gradient(180deg,#3f7f30 0%,#5a9a3c 55%,#3d7a2c 100%)"></div>
  <div class="cap">Jamie Brookfield stretches out to</div>
</div>

<div class="abs sponsors"></div>
<div class="abs badge" style="left:271px;top:848px;width:60px;height:42px;border-radius:50%;background:#555"></div>
<div class="abs badge" style="left:352px;top:853px;width:76px;height:32px;border-radius:16px;background:#8a8a8a"></div>
<div class="abs badge" style="left:451px;top:848px;width:46px;height:46px;border-radius:50%;background:#333"></div>
<div class="abs badge" style="left:528px;top:856px;width:82px;height:28px;background:#555"></div>
<div class="abs badge" style="left:643px;top:853px;width:80px;height:32px;background:#444"></div>
<div class="abs badge" style="left:745px;top:850px;width:66px;height:42px;border-radius:50%;background:#444"></div>
<div class="abs badge" style="left:831px;top:852px;width:40px;height:40px;border-radius:50%;background:#666"></div>

<div class="abs footer-col" style="left:209px;top:925px"><h3>ABOUT US</h3><a href="#">Unions</a><a href="#">Corporations</a><a href="#">Privacy Policy</a><a href="#">Our Sponsors</a></div>
<div class="abs divider" style="left:330px"></div>
<div class="abs footer-col" style="left:354px;top:925px"><h3>PEOPLE</h3><a href="#">Players</a><a href="#">Staff</a><a href="#">Board of Directors</a></div>
<div class="abs divider" style="left:462px"></div>
<div class="abs footer-col" style="left:479px;top:925px"><h3>TEAM PROFILE</h3><a href="#">Squad</a><a href="#">Contact</a></div>
<div class="abs divider" style="left:595px"></div>
<div class="abs footer-col" style="left:612px;top:925px"><h3>FOR FANS</h3><a href="#">Merchandise</a><a href="#">Photos</a></div>
<div class="abs divider" style="left:745px;height:50px"></div>

<div class="abs legal">© 2014 Company Name. All rights reserved.<br><a href="#">Terms &amp; Conditions</a> | <a href="#">Sitemap</a></div>
<div class="abs footer-brand">Apex Harbour<br>Sevens</div>
</body>
</html>
```